fizzy drinks label design

I want to design fizzy drink label for 3 flavors : black grapes, red apple and mojito, band name kestrola, product name KOLTA , product will be in plastic bottle, label size 198 mm X 66mm

```html
<!DOCTYPE html>
<html lang="en">
<head>
<meta charset="utf-8">
<title>kestrola KOLTA fizzy drink labels</title>
<link rel="stylesheet" href="https://fonts.googleapis.com/css2?family=Ubuntu:wght@500;700&family=Oswald:wght@600&display=swap">
<style>
  :root {
    --page: #e6e6e6;
    --silver-light: #f2f2f2;
    --silver-dark: #9a9a9a;
    --white: #ffffff;
  }
  html, body {
    margin: 0;
    width: 1200px;
    height: 900px;
    overflow: hidden;
    background: radial-gradient(ellipse at center, #f7f7f7 0%, var(--page) 70%, #cfcfcf 100%);
  }
  .label-sheet {
    position: relative;
    width: 1200px;
    height: 900px;
  }
  .label {
    position: absolute;
    left: 210px;
    width: 780px;
    height: 260px;
    background: var(--base);
    overflow: hidden;
    box-shadow: 0 4px 14px rgba(0,0,0,0.18);
  }
  .label--grape  { top: 30px;  --base: #6b4cc6; --band: #5536a6; --deep: #4a2e93; --accent: #63d6cb; --art-a: #2e2a3e; --art-b: #7fa850; }
  .label--apple  { top: 320px; --base: #c8171c; --band: #8f0d11; --deep: #a51216; --accent: #f47c20; --art-a: #e3262b; --art-b: #4e9a2d; }
  .label--mojito { top: 610px; --base: #9cc52b; --band: #80a81d; --deep: #8ab523; --accent: #3f5e14; --art-a: #d9e65a; --art-b: #2f8a5a; }

  .label__trim {
    position: absolute;
    left: 0; right: 0;
    height: 7px;
    background: linear-gradient(180deg, var(--silver-light), var(--silver-dark) 60%, var(--silver-light));
  }
  .label__trim--top { top: 0; }
  .label__trim--bottom { bottom: 0; }

  .label__brush-band {
    position: absolute;
    left: 0; right: 0;
    top: 88px;
    height: 86px;
    background: var(--band);
    transform: skewY(-2deg);
  }
  .label__foot-band {
    position: absolute;
    left: 0; right: 0;
    bottom: 7px;
    height: 48px;
    background: var(--deep);
  }

  .label__art {
    position: absolute;
    top: 14px;
    width: 72px;
    height: 230px;
    border-radius: 36px;
    background: linear-gradient(180deg, var(--art-a) 0%, var(--art-b) 35%, var(--art-a) 65%, var(--art-b) 100%);
    opacity: 0.9;
  }
  .label__art--left { left: 248px; }
  .label__art--right { left: 460px; }

  .label__front {
    position: absolute;
    left: 320px;
    width: 140px;
    top: 0;
    height: 260px;
    text-align: center;
    color: var(--white);
  }
  .label__brand {
    margin-top: 28px;
    font-family: "Ubuntu", sans-serif;
    font-weight: 700;
    font-size: 19px;
    line-height: 1;
    color: var(--white);
  }
  .label__product {
    margin-top: 38px;
    font-family: "Ubuntu", sans-serif;
    font-weight: 700;
    font-size: 46px;
    line-height: 1;
    letter-spacing: 1px;
    margin-left: -20px;
    margin-right: -20px;
  }
  .label__rule {
    width: 150px;
    height: 2px;
    margin: 6px auto 0;
    background: var(--white);
  }
  .label__type {
    margin-top: 6px;
    font-family: "Ubuntu", sans-serif;
    font-weight: 500;
    font-size: 15px;
    letter-spacing: 3px;
    color: var(--accent);
    white-space: nowrap;
    margin-left: -20px;
    margin-right: -20px;
  }
  .label__flavor {
    margin-top: 14px;
    font-family: "Oswald", sans-serif;
    font-weight: 600;
    font-style: italic;
    font-size: 15px;
    line-height: 1;
    text-transform: uppercase;
  }
  .label__flavor span { display: block; }
  .label__flavor .label__flavor-accent { color: var(--accent); }
  .label--mojito .label__flavor .label__flavor-accent { color: var(--white); }
  .label__size {
    position: absolute;
    left: 0; right: 0;
    bottom: 24px;
    font-family: "Ubuntu", sans-serif;
    font-weight: 500;
    font-size: 12px;
    letter-spacing: 2px;
  }
</style>
</head>
<body>
<main class="label-sheet">

  <section class="label label--grape" aria-label="KOLTA black grapes label">
    <div class="label__brush-band"></div>
    <div class="label__foot-band"></div>
    <div class="label__trim label__trim--top"></div>
    <div class="label__trim label__trim--bottom"></div>
    <div class="label__art label__art--left" role="img" aria-label="Illustrated black grapes and green leaves"></div>
    <div class="label__art label__art--right" role="img" aria-label="Illustrated black grapes and green leaves"></div>
    <div class="label__front">
      <div class="label__brand">kestrola</div>
      <div class="label__product">KOLTA</div>
      <div class="label__rule"></div>
      <div class="label__type">FIZZY DRINK</div>
      <div class="label__flavor"><span>Black</span><span class="label__flavor-accent">Grapes</span></div>
      <div class="label__size">??? Oz</div>
    </div>
  </section>

  <section class="label label--apple" aria-label="KOLTA red apple label">
    <div class="label__brush-band"></div>
    <div class="label__foot-band"></div>
    <div class="label__trim label__trim--top"></div>
    <div class="label__trim label__trim--bottom"></div>
    <div class="label__art label__art--left" role="img" aria-label="Illustrated red cherries with green leaves"></div>
    <div class="label__art label__art--right" role="img" aria-label="Illustrated red cherries with green leaves"></div>
    <div class="label__front">
      <div class="label__brand">kestrola</div>
      <div class="label__product">KOLTA</div>
      <div class="label__rule"></div>
      <div class="label__type">FIZZY DRINK</div>
      <div class="label__flavor"><span>Red</span><span>Apple</span></div>
      <div class="label__size">??? Oz</div>
    </div>
  </section>

  <section class="label label--mojito" aria-label="KOLTA mojito label">
    <div class="label__brush-band"></div>
    <div class="label__foot-band"></div>
    <div class="label__trim label__trim--top"></div>
    <div class="label__trim label__trim--bottom"></div>
    <div class="label__art label__art--left" role="img" aria-label="Illustrated lemon slices and mint leaves"></div>
    <div class="label__art label__art--right" role="img" aria-label="Illustrated lemon slices and mint leaves"></div>
    <div class="label__front">
      <div class="label__brand">kestrola</div>
      <div class="label__product">KOLTA</div>
      <div class="label__rule"></div>
      <div class="label__type">FIZZY DRINK</div>
      <div class="label__flavor"><span>Mojito</span></div>
      <div class="label__size">??? Oz</div>
    </div>
  </section>

</main>
</body>
</html>
```